Health & Nutrition - Business Cards

Needs to look new-age, simple, and elegant. The cards are for my services/counsel in health and nutrition - which include mind, body, and soul. I would like to see something clean and simple but beautiful. Can have a plain background or with a pattern but I don't want it to take away from my contact details. Therefore, my info can be on the back of the card and a nice front design. I really like the flower of life symbol. The name of my business is called Velvet Meadow.

Target Market(s)

Clients - men & women age 20-60. Adults, parents, teachers, sick individuals seeking nutrient counseling and dietary management.

Industry/Entity Type

Nutritionist

Contact Information for Business Card

Tomas Brindle
Cell: 345-827-4602
Email: tbrindle@quillpost.example

Colors
33a6d7
33b8a4
add136
ffffff
5c5c5c
f04a50
fbee3f
cedeed
85cae6

Requirements
Nice to have
• Maybe it can have some sort of sacred geometry as well, but not required. Nice to have the colors that I choose in the project but feel free to come up with your own use of colors. Thanks! =)

```html
<!DOCTYPE html>
<html lang="en">
<head>
<meta charset="utf-8">
<title>Velvet Meadow — Business Cards</title>
<link rel="stylesheet" href="https://fonts.googleapis.com/css2?family=Work+Sans:wght@400;500;600&display=swap">
<style>
  :root {
    --page-bg: #161616;
    --card-bg: #222222;
    --card-bg-light: #2c2c2c;
    --pattern-dark: #1f1f1f;
    --pattern-light: #4a4a4a;
    --brand-orange: #f07a2a;
    --accent-green: #a8cf36;
    --text-white: #ffffff;
  }
  * { margin: 0; padding: 0; box-sizing: border-box; }
  html, body { width: 1200px; height: 900px; overflow: hidden; }
  body {
    background: var(--page-bg);
    font-family: "Work Sans", sans-serif;
    position: relative;
  }
  .card {
    position: absolute;
    left: 250px;
    width: 700px;
    height: 400px;
    background: linear-gradient(120deg, var(--card-bg) 0%, var(--card-bg) 55%, var(--card-bg-light) 100%);
    overflow: hidden;
  }
  .card--front { top: 35px; }
  .card--back { top: 465px; }

  .pattern-field {
    position: absolute;
    inset: 0;
    background: linear-gradient(100deg, var(--pattern-dark) 0%, #2a2a2a 45%, var(--pattern-light) 100%);
  }
  .brand-name {
    position: absolute;
    color: var(--brand-orange);
    font-weight: 500;
    font-size: 28px;
    letter-spacing: 3px;
    text-transform: uppercase;
    white-space: nowrap;
    line-height: 1.2;
  }
  .card--front .brand-name { left: 0; right: 0; top: 182px; text-align: center; }
  .card--back .brand-name { left: 45px; top: 183px; }

  .divider {
    position: absolute;
    left: 350px;
    top: 130px;
    width: 2px;
    height: 150px;
    background: var(--accent-green);
  }
  .contact-block {
    position: absolute;
    left: 375px;
    top: 140px;
    width: 300px;
    color: var(--text-white);
  }
  .person-name {
    color: var(--accent-green);
    font-weight: 500;
    font-size: 28px;
    letter-spacing: 2px;
    text-transform: uppercase;
    white-space: nowrap;
    line-height: 1.2;
  }
  .person-title {
    font-size: 16px;
    letter-spacing: 1px;
    margin-top: 2px;
    margin-bottom: 16px;
  }
  .contact-line {
    display: flex;
    align-items: center;
    gap: 10px;
    font-size: 16px;
    letter-spacing: 0.5px;
    margin-bottom: 6px;
    white-space: nowrap;
  }
  .contact-icon { width: 13px; height: 13px; flex: none; }
</style>
</head>
<body>
  <section class="card card--front">
    <div class="pattern-field" role="img" aria-label="Embossed flower of life sacred geometry pattern in graphite tones"></div>
    <h1 class="brand-name">Velvet Meadow</h1>
  </section>

  <section class="card card--back">
    <p class="brand-name">Velvet Meadow</p>
    <div class="divider"></div>
    <div class="contact-block">
      <h2 class="person-name">Tomas Brindle</h2>
      <p class="person-title">Director</p>
      <p class="contact-line">
        <svg class="contact-icon" viewBox="0 0 16 16" aria-hidden="true">
          <path d="M4 1 L6 5 L4.5 6.5 Q6 10 9.5 11.5 L11 10 L15 12 L13.5 15 Q6 14.5 1.5 3 Z" fill="#a8cf36"/>
        </svg>
        345-827-4602
      </p>
      <p class="contact-line">
        <svg class="contact-icon" viewBox="0 0 16 16" aria-hidden="true">
          <rect x="1" y="3" width="14" height="10" fill="none" stroke="#a8cf36" stroke-width="1.6"/>
          <path d="M1 3 L8 9 L15 3" fill="none" stroke="#a8cf36" stroke-width="1.6"/>
        </svg>
        tbrindle@quillpost.example
      </p>
      <p class="contact-line">
        <svg class="contact-icon" viewBox="0 0 16 16" aria-hidden="true">
          <circle cx="8" cy="8" r="6.5" fill="none" stroke="#a8cf36" stroke-width="1.4"/>
          <ellipse cx="8" cy="8" rx="3" ry="6.5" fill="none" stroke="#a8cf36" stroke-width="1.2"/>
          <line x1="1.5" y1="8" x2="14.5" y2="8" stroke="#a8cf36" stroke-width="1.2"/>
        </svg>
        www.velvetmeadow.example
      </p>
    </div>
  </section>
</body>
</html>
```